Trifold B2B flyer for software consulting/software futureproofness check / IT company

We need a flyer for a consulting offer for the company "VORANTEK GmbH".

The service involves the analysis and evaluation of software systems in companies; the target group consists of managing directors and IT managers of medium-sized companies in various industries.

The flyer should be modern, uncluttered, serious, and professional. It must inspire trust. A dark background would be preferable.

For content and layout, see PDF/PPTX "Software-Wandel-Fast-Scan-Konzept.pptx|.pdf".

In the appendix you will find further examples of VORANTEK designs, as well as the logo and other images.

-----------
We need a flyer for a consulting offering for the company “VORANTEK GmbH”.

The offering focuses on the analysis and evaluation of software systems within companies. The target audience is managing directors/CEOs and IT managers of mid-sized companies across various industries.

The flyer should be modern, clean, serious, and professional. It must build trust. A dark background is preferred.

Please refer to the PDF/PPTX “Software-Wandels-Fast-Scan-konzept.pptx|.pdf” for the content and the layout/ordering of the sections.

Attached you will also find additional examples of VORANTEK designs, as well as the logo and further images.

Target Market(s)

Medium businesses, various industries. Target group: CEO, CIO, IT lead

Industry/Entity Type

Medium-Businesses, various Industries.

Font styles to use
Sans Serif
Other font styles liked:
• Myriad

Colors

Designer to choose colors to be used in the design.

Requirements
Must have
• Branding of my company, professional, stylish, clean, trustful design

```html
<!DOCTYPE html>
<html lang="de">
<head>
<meta charset="utf-8">
<title>Software-Zukunfts-Quick-Check</title>
<link rel="stylesheet" href="https://fonts.googleapis.com/css2?family=Source+Sans+3:ital,wght@0,400;0,600;0,700;1,400&display=swap">
<style>
  :root {
    --cyan: #3fd4f0;
    --navy: #0f2a44;
    --blue: #1561aa;
    --white: #ffffff;
    --band: #0b2238;
  }
  * { margin: 0; padding: 0; box-sizing: border-box; }
  html, body { width: 1200px; height: 857px; overflow: hidden; background: var(--white); }
  body { font-family: "Source Sans 3", "Myriad Pro", Arial, sans-serif; }

  .flyer { position: relative; width: 1200px; height: 857px; overflow: hidden; }
  .block { position: absolute; }

  .c1 { left: 0; width: 399px; }
  .c2 { left: 399px; width: 399px; }
  .c3 { left: 798px; width: 402px; }
  .top { top: 0; height: 340px; }
  .mid { top: 356px; height: 277px; }
  .bot { top: 649px; height: 208px; }

  .bg-cyan { background: var(--cyan); }
  .bg-navy { background: var(--navy); }
  .bg-blue { background: var(--blue); }
  .bg-white { background: var(--white); }

  .band { position: absolute; left: 0; width: 1200px; height: 16px; background: var(--band); }
  .band-a { top: 340px; }
  .band-b { top: 633px; }

  .frame {
    position: absolute; left: 20px; top: 21px; right: 20px; bottom: 21px;
    border: 1.5px solid rgba(255,255,255,.85); pointer-events: none;
  }

  .title {
    position: absolute; left: 70px; top: 54px;
    color: var(--white); font-size: 29px; font-weight: 400;
  }
  .tagline {
    position: absolute; left: 723px; top: 55px;
    color: var(--white); font-size: 12.5px; font-style: italic;
  }
  .intro {
    position: absolute; left: 70px; top: 117px;
    color: var(--white); font-size: 12.5px; line-height: 1.5;
  }

  .col-head { position: absolute; font-size: 29px; font-weight: 400; line-height: 1.45; }
  .head-questions { left: 44px; top: 279px; color: var(--navy); }
  .head-approach { left: 440px; top: 279px; color: var(--white); }
  .head-results { left: 838px; top: 237px; color: var(--white); }

  .list { position: absolute; list-style: none; font-size: 13.5px; line-height: 18px; }
  .list li { margin-bottom: 10px; padding-left: 8px; text-indent: -8px; }
  .list li::before { content: "• "; }
  .list b { font-weight: 700; }
  .questions { left: 44px; top: 396px; width: 300px; color: var(--white); }
  .approach { left: 438px; top: 396px; width: 275px; color: var(--white); }
  .results { left: 843px; top: 396px; width: 280px; color: var(--navy); }

  .scope { position: absolute; left: 440px; top: 675px; color: var(--white); }
  .scope h3 { font-size: 15px; font-weight: 400; line-height: 1.15; }
  .scope ul { list-style: none; font-size: 9.5px; line-height: 1.35; margin-bottom: 4px; }
  .scope li::before { content: "• "; }
  .scope .cont { padding-left: 7px; }
  .scope .cont::before { content: ""; }

  .price { position: absolute; left: 836px; top: 673px; color: var(--white); }
  .price h3 { font-size: 28px; font-weight: 400; line-height: 1.2; }
  .price ul { list-style: none; font-size: 16px; font-weight: 700; line-height: 1.3; margin: 2px 0 12px 6px; }
  .price li::before { content: "• "; }
  .price p { font-size: 12.5px; line-height: 1.4; width: 290px; margin-left: 6px; }
</style>
</head>
<body>
<div class="flyer">
  <div class="block c1 top bg-cyan"></div>
  <div class="block c2 top bg-navy" role="img" aria-label="Dunkle Fläche mit feinem Diagonalstreifen-Muster"></div>
  <div class="block c3 top bg-blue"></div>

  <div class="band band-a"></div>

  <div class="block c1 mid bg-navy"></div>
  <div class="block c2 mid bg-cyan"></div>
  <div class="block c3 mid bg-white"></div>

  <div class="band band-b"></div>

  <div class="block c1 bot bg-cyan"></div>
  <div class="block c2 bot bg-navy"></div>
  <div class="block c3 bot bg-blue"></div>

  <div class="frame"></div>

  <h1 class="title">Software-Zukunfts-Quick-Check</h1>
  <p class="tagline">Bestandssysteme: weiter investieren, modernisieren oder ersetzen?</p>
  <p class="intro">Der Quick-Check dient der schnellen Orientierung und Objektivierung.<br>
    Er stellt die Basis für eine detaillierte Analyse des Bestandssystems in Punkto Zukunftsfähigkeit und Handlungsoptionen.</p>

  <h2 class="col-head head-questions">Fragestellungen</h2>
  <h2 class="col-head head-approach">Vorgehen</h2>
  <h2 class="col-head head-results">Ergebnisse /<br>Lieferobjekte</h2>

  <ul class="list questions">
    <li>Was sind die <b>realen Risiken</b> (Betrieb, Stabilität, Abhängigkeiten, Know-how)?</li>
    <li>Wo liegen die <b>größten Kostentreiber</b> (Run Kosten, Change-Kosten, Folgekosten)</li>
    <li>Welche drei Wege sind grundsätzlich realistisch: <b>Invest / Modernize / Replace?</b></li>
    <li>Was müssen wir <b>jetzt</b> wissen, um innerhalb von 5–10 Tagen sauber entscheiden zu können?</li>
  </ul>

  <ul class="list approach">
    <li><b>Kickoff (60–90 Min):</b> Ziel, Kontext, Entscheidungsdruck, verfügbare Artefakte</li>
    <li><b>Sichtung &amp; Analyse:</b> max. 10 Artefakte (Kosten, Incidents, Roadmap, Architektur Skizze, Vendor-Info)</li>
    <li><b>2 Interviews (je 60–90 Min):</b> CIO/Owner + Head of Engineering/Tech Lead</li>
    <li><b>Ergebnisgespräch (60 Min):</b> Ergebnisse, Lücken, Empfehlung, nächster Schritt</li>
  </ul>

  <ul class="list results">
    <li><b>Decision Snapshot:</b> Status, Top-Risiken, wesentliche TCO-Treiber, offene Entscheidungsfragen (One-Pager)</li>
    <li><b>3-Optionen-Skizze:</b> Modernize/Replace/Invest mit Pros/Cons und Abhängigkeiten (One-Pager)</li>
    <li><b>Gap-Liste:</b> Welche Informationen fehlen für eine saubere Entscheidung (Max. 10 Punkte)</li>
    <li><b>Go/No-Go-Empfehlung:</b> Mögliche nächste Schritte und Handlungsoptionen</li>
  </ul>

  <div class="scope">
    <h3>Scope:</h3>
    <ul>
      <li>1 System</li>
      <li>1–2 Calls + Doku-Sichtung</li>
      <li>Ergebnis als kompakte Entscheidungsunterlagen</li>
    </ul>
    <h3>Nicht enthalten:</h3>
    <ul>
      <li>Detail-Spezifikation, Ausschreibung, Umsetzung,</li>
      <li class="cont">Tool-Auswahlprozess im Vollumfang</li>
    </ul>
  </div>

  <div class="price">
    <h3>Preis &amp; Dauer:</h3>
    <ul>
      <li>Preis: 3.500–5.000 € (zzgl. USt)</li>
      <li>Dauer: 1 Woche</li>
    </ul>
    <p>Upgrade möglich zum umfassenden <b>Software Zukunfts-Check</b></p>
  </div>
</div>
</body>
</html>
```